Business card for my new company (Accounting firm)

I need a business card for my new business Corvane Advisory and Ledger SA. Our services are accounting, tax, audit and financial management. Our customers are small companies, start-ups and new companies. The final design has to show financial security, trust and growth. Please find our logo attached to the business card. Text for the business card: Corvane Advisory and Ledger SA Tomas da Varela Director and Founder Certified Accountant Tel. 022 418 27 35 tv@corvaneconseil.ch www.corvaneconseil.ch Rue des Vergers-Bleus 14 1201 Geneva
Target Market(s)
Our customers are small companies, start-ups and new companies.
Industry/Entity Type
Finance And Accounting
Contact Information for Business Card
Corvane Conseil et Registre SA
Tomas da Varela
Directeur et Fondateur
Expert-comptable diplômé
Tél. 022 418 27 35
tv@corvaneconseil.ch
www.corvaneconseil.ch
Rue des Vergers-Bleus 14
1201 Genève

```html
<!DOCTYPE html>
<html lang="fr">
<head>
<meta charset="utf-8">
<title>Corvane Conseil et Registre SA – Carte de visite</title>
<link rel="stylesheet" href="https://fonts.googleapis.com/css2?family=Montserrat:wght@400;500;600&display=swap">
<style>
  :root {
    --backdrop: #2b2929;
    --card-white: #ffffff;
    --brand-sky: #34b0e0;
    --brand-navy: #1b6a9a;
    --ink: #3a3a3a;
    --ink-soft: #4a4a4a;
    --rule: #9a9a9a;
  }
  * { margin: 0; padding: 0; box-sizing: border-box; }
  html, body {
    width: 1125px;
    height: 1200px;
    overflow: hidden;
    background: var(--backdrop);
    font-family: "Montserrat", Arial, sans-serif;
  }
  .card {
    position: absolute;
    left: 171px;
    width: 826px;
    height: 472px;
    box-shadow: 0 3px 8px rgba(0,0,0,0.55);
  }
  .card--front { top: 106px; background: var(--card-white); overflow: hidden; }
  .card--back  { top: 639px; background: var(--brand-sky); }

  .brand-name {
    position: absolute;
    left: 100px;
    top: 262px;
    width: 230px;
    text-align: center;
    font-size: 25px;
    font-weight: 600;
    line-height: 1.25;
    color: var(--ink);
  }
  .divider {
    position: absolute;
    left: 357px;
    top: 127px;
    width: 2px;
    height: 210px;
    background: var(--rule);
  }
  .contact {
    position: absolute;
    left: 393px;
    top: 120px;
    color: var(--ink);
  }
  .contact__name {
    font-size: 31px;
    font-weight: 500;
    color: var(--brand-sky);
    line-height: 1.2;
  }
  .contact__role {
    font-size: 20px;
    font-weight: 500;
    line-height: 27px;
  }
  .contact__address {
    margin-top: 16px;
    font-size: 19px;
    line-height: 25px;
    color: var(--ink-soft);
  }
  .contact__lines {
    margin-top: 14px;
    margin-left: 3px;
    font-size: 19.5px;
    font-weight: 500;
    line-height: 27px;
  }
  .footer-band {
    position: absolute;
    left: 0;
    bottom: 0;
    width: 826px;
    height: 40px;
  }
  .website {
    position: absolute;
    left: 231px;
    bottom: 4px;
    width: 379px;
    text-align: center;
    font-size: 19px;
    letter-spacing: 4px;
    color: var(--card-white);
  }
  .back-field {
    position: absolute;
    inset: 0;
    background: linear-gradient(135deg, #37b3e2, #31ade0);
  }
  .back-name {
    position: absolute;
    right: 60px;
    bottom: 80px;
    font-size: 18px;
    font-weight: 600;
    color: var(--card-white);
  }
</style>
</head>
<body>
  <section class="card card--front">
    <div class="brand-name">Corvane Conseil et Registre SA</div>
    <div class="divider"></div>
    <div class="contact">
      <div class="contact__name">Tomas da Varela</div>
      <div class="contact__role">Directeur et Fondateur<br>Expert-comptable diplômé</div>
      <div class="contact__address">Rue des Vergers-Bleus 14<br>1201 Genève</div>
      <div class="contact__lines">P: 022 418 27 35<br>E: tv@corvaneconseil.ch</div>
    </div>
    <svg class="footer-band" viewBox="0 0 826 40" aria-hidden="true">
      <rect x="0" y="31" width="826" height="9" fill="#1b6a9a"/>
      <path d="M231 40 L244 8 Q246 4 251 4 L580 6 Q588 6 591 12 L610 40 Z" fill="#34b0e0"/>
    </svg>
    <div class="website">www.corvaneconseil.ch</div>
  </section>

  <section class="card card--back">
    <div class="back-field" role="img" aria-label="Motif de fond répété de la marque en bleu clair"></div>
    <div class="back-name">Corvane</div>
  </section>
</body>
</html>
```